Full service meeting planning company needs new business cards

Bright Harbor is a full service meeting planning company that specializes in on-line conference registration web development and event communications. We combine citywide hotel management, mobile applications, eblast reminders, confirmation letters, and customized reporting to create a seamless registration process. We also manage group motor coach transportation, food and beverages, entertainment, stage and lighting for group of 10 to 4000.

Target Market(s)

Corporations and associations

Industry/Entity Type

Event Planning

Contact Information for Business Card

standard size 3.5" wide and 2" tall

Font styles to use
Serif
Sans Serif

Colors
f37122
f78f20
333333
5c5c5c
9d9d9d
f68d4d

Requirements
Must have
• {name}
• Bright Harbor
• P.O. Box 7384, Grand Rapids, M I 49577
• www.brightharborplan.com
• {email}
• {phone}
• {mobile phone}
Nice to have
• Our colors are black, grey and orange as an accent color
Should not have
• I am not happy with our website layout anymore either. It feels dark and old but it does explain who we are pretty well if you'd like to review; www.brightharborplan.com

```html
<!DOCTYPE html>
<html lang="en">
<head>
<meta charset="utf-8">
<title>Bright Harbor — Business Card</title>
<link rel="stylesheet" href="https://fonts.googleapis.com/css2?family=Questrial&family=Fira+Sans:wght@600&family=Roboto:wght@400&display=swap">
<style>
  :root {
    --orange: #f37122;
    --orange-light: #f78f20;
    --card-black: #1c1c1e;
    --card-black-soft: #232325;
    --grey-dark: #333333;
    --grey-mid: #5c5c5c;
    --grey-light: #9d9d9d;
    --white: #ffffff;
    --page: #e9e7e4;
  }
  * { margin: 0; padding: 0; box-sizing: border-box; }
  html, body { width: 1200px; height: 716px; overflow: hidden; }
  body { background: var(--page); position: relative; }

  .card {
    position: absolute;
    top: 210px;
    width: 520px;
    height: 297px;
    background: var(--card-black);
    overflow: hidden;
  }
  .card--back { left: 50px; }
  .card--front { left: 630px; }

  /* Back side */
  .back-mark {
    position: absolute;
    left: 50%; top: 50%;
    transform: translate(-50%, -50%);
    display: flex; align-items: center; gap: 14px;
  }
  .back-mark__circle {
    width: 64px; height: 64px; border-radius: 50%;
    background: var(--card-black-soft);
    box-shadow: inset 0 0 0 1px #2c2c2f;
  }
  .back-mark__name {
    font-family: "Questrial", sans-serif;
    font-size: 26px; letter-spacing: 2px;
    color: #2e2e31;
    text-transform: uppercase;
  }

  /* Front side */
  .brand {
    position: absolute; left: 26px; top: 26px;
    display: flex; align-items: center; gap: 12px;
  }
  .brand__circle {
    width: 44px; height: 44px; border-radius: 50%;
    background: var(--orange);
  }
  .brand__name {
    font-family: "Questrial", sans-serif;
    font-size: 24px; letter-spacing: 1.5px;
    color: var(--white);
    text-transform: uppercase;
  }
  .rule {
    position: absolute; left: 26px; top: 108px;
    width: 300px; height: 1px;
    background: var(--orange);
  }
  .contacts {
    position: absolute; left: 26px; top: 124px;
    list-style: none;
    font-family: "Roboto", sans-serif;
    font-size: 12.5px; color: var(--white);
    line-height: 19px;
  }
  .contacts li { display: flex; align-items: center; gap: 8px; }
  .contacts svg { width: 11px; height: 11px; fill: var(--orange); flex: none; }
  .contacts .no-icon { padding-left: 19px; }

  .person {
    position: absolute; right: 26px; top: 140px;
    text-align: right;
    color: var(--white);
  }
  .person__name {
    font-family: "Fira Sans", sans-serif; font-weight: 600;
    font-size: 19px;
  }
  .person__title {
    font-family: "Roboto", sans-serif;
    font-size: 11.5px; margin-top: 3px;
  }
  .address {
    position: absolute; right: 26px; top: 200px;
    text-align: right;
    font-family: "Roboto", sans-serif;
    font-size: 12.5px; line-height: 18px;
    color: var(--white);
  }
  .bands { position: absolute; left: 0; bottom: 0; width: 520px; height: 50px; }
  .bands .band-grey { fill: var(--grey-mid); }
  .bands .band-orange { fill: var(--orange); }
</style>
</head>
<body>
  <section class="card card--back" aria-label="Card back">
    <div class="back-mark">
      <div class="back-mark__circle"></div>
      <span class="back-mark__name">Bright Harbor</span>
    </div>
  </section>

  <section class="card card--front" aria-label="Card front">
    <div class="brand">
      <div class="brand__circle"></div>
      <span class="brand__name">Bright Harbor</span>
    </div>
    <div class="rule"></div>
    <ul class="contacts">
      <li><svg viewBox="0 0 24 24"><path d="M6.6 10.8a15 15 0 0 0 6.6 6.6l2.2-2.2a1 1 0 0 1 1-.25 11 11 0 0 0 3.6.6 1 1 0 0 1 1 1V20a1 1 0 0 1-1 1A17 17 0 0 1 3 4a1 1 0 0 1 1-1h3.5a1 1 0 0 1 1 1 11 11 0 0 0 .6 3.6 1 1 0 0 1-.25 1z"/></svg>616 555 0142 x11</li>
      <li><svg viewBox="0 0 24 24"><path d="M7 2h10a1 1 0 0 1 1 1v18a1 1 0 0 1-1 1H7a1 1 0 0 1-1-1V3a1 1 0 0 1 1-1zm1 3v13h8V5z"/></svg>616 555 0187</li>
      <li><svg viewBox="0 0 24 24"><path d="M2 5h20v14H2zm2 2v.5l8 5 8-5V7z"/></svg>info@brightharborplan.com</li>
      <li><svg viewBox="0 0 24 24"><circle cx="12" cy="12" r="10"/></svg>www.brightharborplan.com</li>
    </ul>
    <div class="person">
      <div class="person__name">Dana Rowley</div>
      <div class="person__title">CMP, Sr. Project Manager</div>
    </div>
    <div class="address">P.O. Box 7384<br>Grand Rapids, M I 49577</div>
    <svg class="bands" viewBox="0 0 520 50" aria-hidden="true">
      <rect class="band-grey" x="0" y="14" width="270" height="36"/>
      <polygon class="band-orange" points="238,50 280,4 520,4 520,50"/>
    </svg>
  </section>
</body>
</html>
```